Cloud Hosting Provider Web Site

We need to create the design for Nimbo-Pails.net a new Cloud Hosting Provider Website.

We already have a logo and a draft website with preliminary content showing the desired structure for the final web site.

I need a design for the Home Page and all 10 Internal web pages currently linked from the draft home page.

The documentation site (/docs) Customer Portal (/portal) and Support site (/support) are not part of this design project.

We need images to illustrate all pages which of course need to be consistent with the content. Please read carefully the text of each page in the draft web site to understand the purpose of each page and illustrate it accordingly.

All pages must be illustrated with images, I do not want any single page with just text.

I want to maintain the slides idea of the draft website home page.

The web site must look professional, we are competitors of huge companies like tallow grid systems (tgs.tallowgrid.com), Velquist Oriel (oriel.velquist.com) and DuneLoft (www.duneloft.com) so we need to look as serious as them.

You may download the draft web site pages to style them, I need fully finalized HTML / CSS and image files.

A top link bar and link footer must be included in every page.

Also the web site will have the possibility to start a chat conversation with a sales agent, so a graphical link to do so must be included in the design, together with a chat window design (including HTML/CSS)

Information for accessing the draft web site follows:

URL: www.nimbo-pails.net
username: design
password: QOPqop987654

If you need any additional information please let me know.

```html
<!DOCTYPE html>
<html lang="en">
<head>
<meta charset="utf-8">
<title>Nimbo-Pails.net – Cloud Hosting</title>
<link href="https://fonts.googleapis.com/css2?family=Anton&family=Lato:ital,wght@0,300;0,400;0,700;1,400&family=PT+Sans:ital,wght@0,400;0,700;1,400&display=swap" rel="stylesheet">
<style>
:root{
  --sky:#1e9ee0;
  --sky-dark:#1580c4;
  --navy:#17325e;
  --red:#e0242b;
  --charcoal:#2b2b2b;
  --ink:#1f1f1f;
  --footer:#333436;
  --base:#232323;
  --mist:#f1f2f4;
  --grey-text:#6b6f74;
  --soft-white:#e8e8e8;
  --footer-text:#b5b6b8;
}
*{margin:0;padding:0;box-sizing:border-box}
html,body{width:1200px;height:2296px;overflow:hidden;background:#fff}
body{font-family:"PT Sans",Arial,sans-serif;color:var(--ink)}
.canvas{position:relative;width:1200px;height:2296px;overflow:hidden}
.abs{position:absolute}

/* top bar */
.topbar{left:0;top:0;width:1200px;height:32px;background:var(--sky);color:#fff;font-size:12px}
.topbar .item{position:absolute;top:8px;display:flex;align-items:center;gap:8px;white-space:nowrap}
.topbar svg{width:16px;height:16px}
.social{display:flex;gap:6px}
.social span{display:block;width:24px;height:24px;border-radius:3px}
.topbar .social{position:absolute;left:922px;top:4px}

/* header */
.header{left:0;top:32px;width:1200px;height:76px;background:var(--charcoal)}
.brand{position:absolute;left:166px;top:16px;display:flex;align-items:center;gap:10px;color:#fff;font-weight:700;font-size:25px;white-space:nowrap}
.brand-mark{width:40px;height:40px;border-radius:50%;background:var(--sky)}
.account{position:absolute;left:874px;top:10px;display:flex}
.account span{font-size:11px;font-weight:700;padding:4px 18px;color:#fff}
.login{background:var(--sky);border-radius:12px 0 0 12px}
.register{background:#fff;color:var(--ink)!important;border-radius:0 12px 12px 0}
.nav{position:absolute;left:442px;top:36px;display:flex;height:40px;font-size:12px;color:#fff}
.nav a{display:flex;align-items:center;padding:0 15px;color:#fff;text-decoration:none;text-transform:uppercase;white-space:nowrap}
.nav a.active{background:var(--sky);height:76px;margin-top:-36px;padding-top:36px}

/* hero */
.hero{left:0;top:108px;width:1200px;height:400px;background:linear-gradient(100deg,#d9e3ea 0%,#eef3f6 45%,#c9d6df 100%)}
.hero-person{left:712px;top:150px;width:318px;height:340px;background:linear-gradient(180deg,#b8c3cc,#6e7680)}
.hero-title{left:188px;top:162px;font-family:"Anton",Impact,sans-serif;font-size:40px;font-style:italic;font-weight:400;color:#fff;letter-spacing:1px;text-shadow:2px 2px 0 #555;white-space:nowrap}
.hero-title em{color:var(--sky)}
.hero-lede{left:190px;top:230px;width:540px;font-size:14px;line-height:22px;color:#222}
.perks{left:228px;top:292px;list-style:none;font-size:13px;color:#222}
.perks li{height:26px;display:flex;align-items:center;gap:16px;white-space:nowrap}
.btn{position:absolute;display:flex;align-items:center;justify-content:center;color:#fff;font-size:13px;text-transform:uppercase;border-radius:3px}
.btn-red{left:190px;top:436px;width:132px;height:36px;background:var(--red)}
.btn-navy{left:336px;top:436px;width:134px;height:36px;background:var(--navy)}

/* about band */
.about{left:0;top:470px;width:1200px;height:410px}
.about-title{font-size:24px;font-weight:400;white-space:nowrap}
.who{left:182px;top:580px;color:#fff}
.who .rule{width:270px;height:1px;background:#fff;margin-top:6px}
.who-text{left:182px;top:642px;width:400px;color:#fff;font-size:13px;line-height:22px;text-align:justify}
.who-list{left:196px;top:742px;color:#fff;font-size:12px;list-style:none}
.who-list li{height:24px;display:flex;align-items:center;gap:10px;white-space:nowrap}
.who-list li::before{content:"";width:6px;height:6px;border-radius:50%;background:#fff}
.more{left:450px;top:812px;width:140px;height:30px;background:#fff;border-radius:15px;color:#555;font-size:12px;display:flex;align-items:center;justify-content:center}
.why{left:828px;top:580px;color:#555}
.why .rule{width:190px;height:1px;background:#999;margin-top:6px}
.why-list{left:708px;top:646px;list-style:none;font-size:13px;color:#555}
.why-list li{height:28.5px;display:flex;align-items:center;gap:30px;white-space:nowrap}
.why-list .ico{width:18px;height:18px;border:2px solid var(--sky-dark);border-radius:3px}

/* power */
.power{left:0;top:880px;width:1200px;height:510px;background:linear-gradient(180deg,#1b1b1b,#3a3d40 55%,#1d1d1d)}
.power-title{left:0;top:940px;width:1200px;text-align:center;font-family:"Lato",sans-serif;font-weight:300;font-size:36px;color:var(--sky);letter-spacing:2px}
.service{position:absolute;top:1054px;width:220px;text-align:center;color:#fff}
.service svg{width:56px;height:72px}
.service h3{font-size:16px;font-weight:700;margin-top:28px;white-space:nowrap}
.service p{font-size:12.5px;line-height:17px;color:#ddd;margin:12px auto 0;width:180px}
.service .know{position:absolute;left:55px;top:258px;width:110px;height:26px;background:var(--sky);border-radius:13px;font-size:11px;display:flex;align-items:center;justify-content:center}

/* testimonial */
.testimonial{left:0;top:1390px;width:1200px;height:302px;background:var(--charcoal)}
.avatar{left:550px;top:1412px;width:100px;height:100px;border-radius:50%;border:4px solid #fff;background:linear-gradient(180deg,#9aa5ae,#5d656d)}
.quote{left:300px;top:1530px;width:600px;font-style:italic;color:var(--soft-white);font-size:14px;line-height:22px;text-align:center}
.cite{left:0;top:1592px;width:1200px;text-align:center;font-size:11px;color:#777;font-style:italic}
.dots{left:584px;top:1634px;display:flex;gap:10px}
.dots span{width:8px;height:8px;background:#555}
.dots span:first-child{background:var(--sky)}

/* clients */
.clients{left:0;top:1692px;width:1200px;height:298px;background:linear-gradient(180deg,#fff,#f3f4f6)}
.clients-title{left:0;top:1734px;width:1200px;text-align:center;font-family:"Lato",sans-serif;font-variant:small-caps;font-size:40px;color:var(--sky);letter-spacing:2px}
.client{position:absolute;top:1818px;width:156px;height:88px;background:#fff;border:5px solid #e2e3e6;border-radius:10px;display:flex;align-items:center;justify-content:center;gap:8px;font-size:17px;font-weight:700;color:#333;white-space:nowrap}
.client i{width:18px;height:18px;background:#333;display:block}
.pager{top:1928px;width:26px;height:26px;border-radius:50%;background:#dcdde0}

/* links band */
.links{left:0;top:1990px;width:1200px;height:58px;background:var(--sky-dark);color:#fff;display:flex;align-items:center;justify-content:center;gap:14px;font-family:"Lato",sans-serif;font-variant:small-caps;font-size:19px;white-space:nowrap}

/* footer */
.footer{left:0;top:2048px;width:1200px;height:184px;background:var(--footer)}
.fcol-title{position:absolute;top:2076px;font-size:16px;font-weight:400;color:#ccc;text-decoration:underline;white-space:nowrap}
.frow{position:absolute;display:flex;align-items:center;gap:12px;font-size:11px;color:var(--footer-text);white-space:nowrap}
.frow i{width:22px;height:22px;border-radius:50%;background:#6a6b6d;display:block;flex:none}
.chat-note{left:584px;top:2150px;width:200px;text-align:center;color:var(--footer-text);font-size:11px;line-height:16px}
.subscribe{left:826px;top:2110px;width:212px;height:36px;background:#4a4b4d;border-radius:3px;font-size:11px;color:#999;padding:11px 10px}
.subscribe-btn{left:948px;top:2158px;width:90px;height:26px;background:var(--sky);color:#fff;font-size:11px;border-radius:3px;display:flex;align-items:center;justify-content:center}

/* base bar */
.base{left:0;top:2232px;width:1200px;height:64px;background:var(--base);color:#aaa;font-size:11px}
.base p{white-space:nowrap}
.base .social{position:absolute;left:890px;top:18px;gap:10px}
.base .social span{width:30px;height:30px}
</style>
</head>
<body>
<div class="canvas">

  <div class="abs topbar">
    <div class="item" style="left:176px"><svg viewBox="0 0 16 16"><path d="M4 1l3 3-2 2c1 2 3 4 5 5l2-2 3 3-2 3C7 15 1 9 1 3z" fill="#fff"/></svg>Call Us: (01) 4826 3190</div>
    <div class="item" style="left:362px"><svg viewBox="0 0 16 16"><rect x="1" y="3" width="14" height="10" fill="#fff"/><path d="M1 3l7 6 7-6" stroke="#1e9ee0" fill="none"/></svg>E-mail Us: support@nimbopails.net</div>
    <div class="item" style="left:596px"><svg viewBox="0 0 16 16"><path d="M1 3h10v7H5l-3 3v-3H1z" fill="#fff"/><path d="M12 6h3v6h-1v2l-2-2H7v-1h5z" fill="#fff"/></svg>Live Chat Support</div>
    <div class="item" style="left:758px"><svg viewBox="0 0 16 16"><path d="M2 14l8-8M10 2a4 4 0 004 4l-3 3-3-3z" stroke="#fff" stroke-width="2" fill="none"/></svg>24 X 7 X 365 Support</div>
    <div class="social"><span style="background:#3b5998"></span><span style="background:#1da1f2"></span><span style="background:#0e76a8"></span><span style="background:#d34836"></span></div>
  </div>

  <header class="abs header">
    <div class="brand"><span class="brand-mark"></span>Nimbo-Pails.net</div>
    <div class="account"><span class="login">LOG IN</span><span class="register">REGISTER</span></div>
    <nav class="nav">
      <a class="active">Home</a><a>Use Cases ▾</a><a>Cloud Services ▾</a><a>Pail's Infrastructure ▾</a><a>About Us</a>
    </nav>
  </header>

  <section class="abs hero" role="img" aria-label="Bright modern office interior with desks and plants"></section>
  <div class="abs hero-person" role="img" aria-label="Smiling businessman in a grey suit with arms crossed"></div>
  <h1 class="abs hero-title">WELCOME TO <em>NIMBO-PAILS</em></h1>
  <p class="abs hero-lede">Lorem ipsum dolor sit amet, consectetur adipisicing elit, sed do eiusmod tempor incididunt ut labore et dolore magna aliqua.</p>
  <ul class="abs perks">
    <li><span>→</span>Unlimited Web Space</li>
    <li><span>→</span>Unlimited Bandwidth (Data Transfer)</li>
    <li><span>→</span>Host Unlimited Domains on 1 Account</li>
    <li><span>→</span>Unlimited E-mail Accounts</li>
  </ul>
  <div class="btn btn-red">Read More</div>
  <div class="btn btn-navy">View Plans</div>

  <svg class="abs about" viewBox="0 0 1200 410" preserveAspectRatio="none">
    <polygon points="0,0 600,90 1200,0 1200,410 0,410" fill="#f1f2f4"/>
    <polygon points="0,22 606,104 606,410 0,410" fill="#2aa0e6"/>
    <polygon points="0,0 600,90 600,104 0,22" fill="#1580c4"/>
    <polygon points="600,90 1200,0 1200,18 612,104" fill="#1e9ee0"/>
  </svg>
  <div class="abs who"><h2 class="about-title">Who We Are</h2><div class="rule"></div></div>
  <p class="abs who-text">We have been in the Market since 2.009, in that time we were focused in dedicated physical servers but since 2.012 we have moved to private virtualization platforms.</p>
  <ul class="abs who-list"><li>100% power uptime since 2.011</li><li>100% network uptime since 2.011</li><li>242 Gbps network capacity</li></ul>
  <div class="abs more">More Details...</div>
  <div class="abs why"><h2 class="about-title">Why Choose Us ?</h2><div class="rule"></div></div>
  <ul class="abs why-list">
    <li><span class="ico"></span>24 x 7 x 365 Support</li>
    <li><span class="ico"></span>Affordable Prices</li>
    <li><span class="ico"></span>No Overload Servers</li>
    <li><span class="ico"></span>Secure &amp; Instant Order Process</li>
    <li><span class="ico"></span>Satisfied Customers</li>
    <li><span class="ico"></span>Industry Best Accreditations</li>
    <li><span class="ico"></span>Hosting since 2009</li>
  </ul>

  <section class="abs power" role="img" aria-label="Dim data centre aisle lined with server racks"></section>
  <h2 class="abs power-title">THE POWER OF CLOUD HOSTING</h2>
  <div class="service" style="left:140px">
    <svg viewBox="0 0 56 72"><path d="M28 72L10 48A28 28 0 1146 48z" fill="#fff"/><circle cx="28" cy="28" r="22" fill="#1580c4"/><rect x="17" y="18" width="22" height="6" rx="2" fill="#fff"/><rect x="17" y="26" width="22" height="6" rx="2" fill="#fff"/><rect x="17" y="34" width="22" height="6" rx="2" fill="#fff"/></svg>
    <h3>Public Cloud Hosting</h3><p>Create your own virtual server using public cloud hosting</p><div class="know">Know More</div>
  </div>
  <div class="service" style="left:366px">
    <svg viewBox="0 0 56 72"><path d="M28 72L10 48A28 28 0 1146 48z" fill="#fff"/><circle cx="28" cy="28" r="22" fill="#1580c4"/><circle cx="21" cy="28" r="6" fill="none" stroke="#fff" stroke-width="3"/><path d="M27 28h12v5M34 28v4" stroke="#fff" stroke-width="3" fill="none"/></svg>
    <h3>Private Cloud Hosting</h3><p>You can secure your hosting through private cloud hosting with some amazing protection.</p><div class="know">Know More</div>
  </div>
  <div class="service" style="left:594px">
    <svg viewBox="0 0 56 72"><path d="M28 72L10 48A28 28 0 1146 48z" fill="#fff"/><circle cx="28" cy="28" r="22" fill="#1580c4"/><ellipse cx="28" cy="19" rx="11" ry="4" fill="#fff"/><rect x="17" y="23" width="22" height="6" rx="2" fill="#fff"/><rect x="17" y="31" width="22" height="6" rx="2" fill="#fff"/></svg>
    <h3>Business Cloud Hosting</h3><p>Business Cloud Hosting is a complete IT support for your business with the combination of Public &amp; Private Cloud Hosting.</p><div class="know">Know More</div>
  </div>
  <div class="service" style="left:826px">
    <svg viewBox="0 0 56 72"><path d="M28 72L10 48A28 28 0 1146 48z" fill="#fff"/><circle cx="28" cy="28" r="22" fill="#1580c4"/><path d="M18 24a10 10 0 0120 0h1a5 5 0 010 10H17a5 5 0 010-10z" fill="#fff"/><rect x="19" y="34" width="18" height="5" fill="#fff"/></svg>
    <h3>Cloud Storage Hosting</h3><p>Cloud storage hosting will backup your all digital data, sync it across all devicess and make share super easy.</p><div class="know">Know More</div>
  </div>

  <section class="abs testimonial"></section>
  <div class="abs avatar" role="img" aria-label="Portrait of a client giving a testimonial"></div>
  <p class="abs quote">Lorem Ipsum is simply dummy text of the printing and typesetting industry. Lorem Ipsum has been the industry's standard dummy text ever since the 1500s, when an unknown printer took a galley .</p>
  <p class="abs cite">Mr. L. Ferrand - Tessaly - www.tessaly.net</p>
  <div class="abs dots"><span></span><span></span><span></span></div>

  <section class="abs clients"></section>
  <h2 class="abs clients-title">Our Esteemed Clients</h2>
  <div class="client" style="left:164px">Vantrel</div>
  <div class="client" style="left:344px"><i></i>Harlow Penn</div>
  <div class="client" style="left:524px">Qorvi</div>
  <div class="client" style="left:704px">Vantrel</div>
  <div class="client" style="left:884px"><i></i>Harlow Penn</div>
  <div class="abs pager" style="left:562px"></div>
  <div class="abs pager" style="left:610px"></div>

  <nav class="abs links">
    <span>Cloud Pricing</span>|<span>Cloud Cost Calculator</span>|<span>Cloud Apps</span>|<span>Cloud Backup</span>|<span>Build Your Own Cloud Server</span>
  </nav>

  <footer class="abs footer"></footer>
  <h3 class="fcol-title" style="left:160px">Sales Information</h3>
  <div class="frow" style="left:160px;top:2112px"><i></i>(01) 4826 3190</div>
  <div class="frow" style="left:160px;top:2142px"><i></i>(02) 7153 0648</div>
  <div class="frow" style="left:160px;top:2172px"><i></i>Email : sales@nimbopails.net</div>
  <h3 class="fcol-title" style="left:380px">Members Support</h3>
  <div class="frow" style="left:380px;top:2112px"><i></i>(01) 4826 3190</div>
  <div class="frow" style="left:380px;top:2142px"><i></i>(02) 7153 0648</div>
  <div class="frow" style="left:380px;top:2172px"><i></i>Email : sales@nimbopails.net</div>
  <h3 class="fcol-title" style="left:584px">Live Chat Now</h3>
  <div class="frow" style="left:584px;top:2112px"><i style="border-radius:4px"></i>live chat support with our experts</div>
  <p class="abs chat-note">You can chat with our experts<br>Anytime, Anywhere.</p>
  <h3 class="fcol-title" style="left:826px">Subscribe Newsletter</h3>
  <div class="abs subscribe">Email Address ...</div>
  <div class="abs subscribe-btn">SUBSCRIBE</div>

  <div class="abs base">
    <p class="abs" style="left:164px;top:12px">FAQs &nbsp;|&nbsp; Privacy Policy &nbsp;|&nbsp; Terms of Services &nbsp;|&nbsp; Sitemap &nbsp;|&nbsp; Blog</p>
    <p class="abs" style="left:164px;top:34px">© 2015 Nimbo-pails.net . All rights reserved.</p>
    <div class="social"><span style="background:#3b5998"></span><span style="background:#d34836"></span><span style="background:#1da1f2"></span><span style="background:#0e76a8"></span></div>
  </div>

</div>
</body>
</html>
```